依頼詳細
「あなたの会社の近くに、こんないい足場会社があるよ」ということを伝えるチラシ
良い足場会社とは
資材を潤沢に持っているのでいつでも資材切れを起こさない
頼めばすぐ来てくれる(見積もり、施工)
早く、正確な施工
安全・安心
です。それらを惹起させるチラシの作成をお願いします。

一般住宅から、高層ビル・特殊な現場も請け負い可能
「安全かつ作業効率のいい足場」を提供
などの文言が入るといいです

チラシ配布対象者
工務店の現場監督さん、購買担当者さんです。

弊社の特徴
右肩上がりで成長している会社
くさび式足場を使用
記載項目
「とび工事一式・足場材リース」
建設業許可番号
社名、電話、FAX、メールアドレス、HP
材工一式(材料も施工も自社で行う、という意味)
サイズ
A4
ページ数
片面
希望イメージ
シンプル 複雑
単色 カラフル
暗い 明るい
日常 高級
遊び心 厳粛
未来的 伝統的
女性的 男性的
希望する色
青系
納品ファイル
• イラストレーター形式 (.ai)
補足説明

お客様の目に留まりやすそうなデザインで、配色がきれいで気に入りましたにいりました。
また修正も素早く対応いただきありがとうございました。

素敵なチラシをご提案いただきありがとうございました。

```html
<!DOCTYPE html>
<html lang="ja">
<head>
<meta charset="UTF-8">
<title>青嶺工業 足場チラシ</title>
<link href="https://fonts.googleapis.com/css2?family=Noto+Sans+JP:wght@400;500;700;900&display=swap" rel="stylesheet">
<style>
:root{
  --navy:#0d2a6b;
  --blue:#1f63c6;
  --sky:#3fa2e8;
  --red:#e0191e;
  --orange:#f08a00;
  --white:#ffffff;
  --ink:#1c2433;
  --pale:#eaf4fc;
}
*{box-sizing:border-box;margin:0;padding:0}
html,body{width:873px;height:1200px;overflow:hidden;background:#fff}
body{font-family:"Noto Sans JP",sans-serif;color:var(--ink)}
.flyer{position:relative;width:873px;height:1200px;overflow:hidden;background:var(--white)}

.hero-photo{position:absolute;left:0;top:0;width:873px;height:370px;
  background:linear-gradient(160deg,#dfeefa 0%,#a9c8e6 45%,#6e97c4 100%)}
.brand-tag{position:absolute;left:18px;top:14px;background:var(--white);padding:6px 14px;
  display:flex;align-items:center;gap:8px;font-weight:900;font-size:22px;color:var(--navy)}
.brand-tag .corp{font-size:12px;font-weight:700}
.brand-dot{width:16px;height:16px;background:var(--navy);border-radius:50%;flex:none}

.headline{position:absolute;left:0;top:185px;width:873px;padding-left:70px;
  font-weight:900;line-height:1;color:var(--navy);
  -webkit-text-stroke:10px var(--white);paint-order:stroke fill}
.headline .row{display:block;white-space:nowrap}
.headline .big{font-size:104px;color:var(--red)}
.headline .mid{font-size:82px}
.headline .row2{margin-top:-6px}
.tagline{position:absolute;top:400px;left:0;width:873px;text-align:center;font-size:26px;font-weight:700;
  color:var(--navy);-webkit-text-stroke:6px var(--white);paint-order:stroke fill}

.mid-photo{position:absolute;left:0;top:370px;width:873px;height:470px;
  background:linear-gradient(180deg,#8fb6dc 0%,#5f8fc4 40%,#2f5e9e 100%)}
.mid-shade{position:absolute;left:0;top:440px;width:873px;height:400px;background:rgba(20,60,130,.35)}

.zaiko{position:absolute;left:235px;top:460px;width:400px;height:95px;background:var(--orange);
  border:4px solid var(--white);display:flex;align-items:center;justify-content:center;
  font-size:66px;font-weight:900;color:var(--white);letter-spacing:18px;padding-left:18px}
.method{position:absolute;left:150px;top:565px;width:573px;height:44px;background:var(--navy);
  color:var(--white);font-size:28px;font-weight:900;text-align:center;line-height:44px;letter-spacing:2px}
.services{position:absolute;left:62px;top:622px;width:750px;display:flex;gap:14px}
.service{flex:1;height:54px;background:linear-gradient(180deg,#2f8fe0,#1a5fb8);border:3px solid var(--white);
  color:var(--white);font-size:27px;font-weight:900;display:flex;align-items:center;justify-content:center}

.scopes{position:absolute;left:62px;top:692px;width:750px;display:grid;grid-template-columns:1fr 1fr;gap:10px 14px}
.scope{height:34px;background:var(--white);border-left:10px solid var(--sky);display:flex;align-items:center;
  padding-left:14px;font-size:17px;font-weight:700;color:var(--navy);position:relative}
.scope::after{content:"";position:absolute;right:10px;top:11px;border-left:10px solid var(--sky);
  border-top:6px solid transparent;border-bottom:6px solid transparent}

.about{position:absolute;left:60px;top:852px;width:753px;font-size:19px;line-height:1.65;font-weight:500;color:var(--ink)}

.call-band{position:absolute;left:0;top:932px;width:873px;height:120px;background:var(--pale)}
.call-sub{position:absolute;left:0;top:938px;width:873px;text-align:center;font-size:30px;font-weight:900;color:var(--blue)}
.call-main{position:absolute;left:40px;top:982px;width:793px;height:64px;background:var(--orange);
  color:var(--white);font-size:52px;font-weight:900;text-align:center;line-height:64px;letter-spacing:2px}

.footer{position:absolute;left:0;top:1056px;width:873px;height:144px;background:var(--white)}
.f-brand{position:absolute;left:24px;top:8px;display:flex;align-items:center;gap:8px}
.f-brand .name{font-size:30px;font-weight:900;color:var(--navy)}
.f-brand .corp{font-size:13px;font-weight:700;color:var(--navy)}
.f-meta{position:absolute;left:56px;top:54px;font-size:14px;font-weight:700;color:var(--navy);line-height:1.4}
.f-small{position:absolute;left:24px;top:104px;font-size:11px;color:#555}
.f-tel{position:absolute;left:440px;top:4px;display:flex;flex-direction:column;gap:2px}
.tel-row{display:flex;align-items:center;gap:10px;font-size:40px;font-weight:900;color:var(--blue);line-height:46px;white-space:nowrap}
.tel-row svg{width:34px;height:34px;flex:none}
.link-row{position:absolute;display:flex;align-items:center;gap:6px;font-size:11px;line-height:14px;color:#333;white-space:nowrap}
.link-web{left:300px;top:108px}
.link-mail{left:300px;top:126px}
.link-social{left:560px;top:108px}
</style>
</head>
<body>
<main class="flyer">
  <div class="hero-photo" role="img" aria-label="足場の上に立つ作業員と建設中の建物の写真"></div>
  <div class="brand-tag"><span class="brand-dot"></span><span class="corp">株式会社</span>青嶺工業</div>

  <div class="mid-photo" role="img" aria-label="くさび式足場が組まれた建築現場の写真"></div>
  <div class="mid-shade"></div>

  <h1 class="headline">
    <span class="row"><span class="big">建物</span><span class="mid">の数だけ</span></span>
    <span class="row row2"><span class="big">足場</span><span class="mid">がある!!</span></span>
  </h1>
  <p class="tagline">〜安全は全てにおいて最優先〜</p>

  <div class="zaiko">材工一式</div>
  <div class="method">くさび式足場法式採用</div>
  <div class="services">
    <div class="service">鳶工事一式</div>
    <div class="service">足場材リース</div>
    <div class="service">鉄骨工事</div>
  </div>
  <div class="scopes">
    <div class="scope">一戸建て住宅新築工事の足場架設</div>
    <div class="scope">解体工事現場の足場架設</div>
    <div class="scope">ビル建設工事の足場架設</div>
    <div class="scope">新幹線工事現場の足場架設</div>
    <div class="scope">架構積極工事の吊り足場架設</div>
    <div class="scope">ビル建築工事の鉄骨の組み上げ</div>
  </div>

  <p class="about">小規模工事から大規模工事まで幅広く様々な現場・工法に応じた架設工事や鉄骨工事、太陽光発電所の設置工事などに携わり、施工や現場管理のサポートを行っています。</p>

  <div class="call-band"></div>
  <p class="call-sub">足場のことなら</p>
  <p class="call-main">おまかせください!</p>

  <footer class="footer">
    <div class="f-brand"><span class="brand-dot"></span><span class="corp">株式会社</span><span class="name">青嶺工業</span></div>
    <div class="f-meta">とび・土木工事業<br>北陸県知事許可第00000号</div>
    <div class="f-small">代表者 山田</div>
    <div class="f-tel">
      <div class="tel-row">
        <svg viewBox="0 0 24 24"><path fill="#f08a00" d="M6.6 10.8a15 15 0 0 0 6.6 6.6l2.2-2.2c.3-.3.7-.4 1-.2 1.1.4 2.3.6 3.6.6.6 0 1 .4 1 1V20c0 .6-.4 1-1 1A17 17 0 0 1 3 4c0-.6.4-1 1-1h3.5c.6 0 1 .4 1 1 0 1.3.2 2.5.6 3.6.1.3 0 .7-.2 1z"/></svg>
        076-000-1120
      </div>
      <div class="tel-row">
        <svg viewBox="0 0 24 24"><rect x="6" y="3" width="12" height="6" fill="#1f63c6"/><rect x="3" y="9" width="18" height="9" rx="2" fill="#1f63c6"/><rect x="7" y="14" width="10" height="7" fill="#fff" stroke="#1f63c6" stroke-width="1.5"/></svg>
        076-000-1121
      </div>
    </div>
    <div class="link-row link-web">
      <svg width="14" height="14" viewBox="0 0 24 24"><circle cx="12" cy="12" r="10" fill="none" stroke="#1f63c6" stroke-width="2"/><path d="M2 12h20M12 2c3 3 3 17 0 20M12 2c-3 3-3 17 0 20" fill="none" stroke="#1f63c6" stroke-width="1.5"/></svg>
      http://www.aomine-kogyo.example
    </div>
    <div class="link-row link-mail">
      <svg width="14" height="14" viewBox="0 0 24 24"><rect x="2" y="5" width="20" height="14" fill="none" stroke="#1f63c6" stroke-width="2"/><path d="M2 5l10 8 10-8" fill="none" stroke="#1f63c6" stroke-width="2"/></svg>
      info@aomine-kogyo.example
    </div>
    <div class="link-row link-social">
      <span style="width:14px;height:14px;border-radius:50%;background:#1f63c6;display:inline-block"></span>
      https://social.example/aominekogyo/
    </div>
  </footer>
</main>
</body>
</html>
```